New Business Cards for Organic Meat Farm

We need a business card designed for Quillmere Farm, a meat farm in western MA. Our logo uses a hand-drawn woodcut (attached). Our color palette has been simply black and white (shown in notepad and picture of our food truck). While we are based out of western MA, we have ambitions to grow nationally, so our hope is for a classy and memorable card which will be printed on a premium quality stock from a printer like printkestrel.com.
Target Market(s)
consumers of quality meats, restauranteurs, partnering farms
Industry/Entity Type
Farming and prepared meat products
Contact Information for Business Card
Alder Vossen, President/Owner, wendell@thornburyfarm.com, mobile: 413-555-0172, phone: 413-555-0148, thornburyfarm.com, facebook: @thornburyfarm, instagram: @thornburyfarmma
Colors
Designer to choose colors to be used in the design.
Look and feel

```html
<!DOCTYPE html>
<html lang="en">
<head>
<meta charset="utf-8">
<title>Quillmere Farm — Business Cards</title>
<link href="https://fonts.googleapis.com/css2?family=Oswald:wght@400;500&display=swap" rel="stylesheet">
<style>
  :root {
    --page: #ffffff;
    --card: #033044;
    --ink: #ffffff;
  }
  * { margin: 0; padding: 0; box-sizing: border-box; }
  html, body {
    width: 1200px;
    height: 1200px;
    overflow: hidden;
    background: var(--page);
  }
  .sheet {
    position: relative;
    width: 1200px;
    height: 1200px;
  }
  .card {
    position: absolute;
    left: 352px;
    width: 496px;
    height: 283px;
    background: var(--card);
    color: var(--ink);
    font-family: "Oswald", sans-serif;
  }
  .card--top { top: 273px; }
  .card--bottom { top: 644px; }

  .brand {
    position: absolute;
    left: 66px;
    top: 66px;
    width: 152px;
    height: 152px;
    border: 3px solid var(--ink);
    border-radius: 50%;
    display: flex;
    align-items: center;
    justify-content: center;
    text-align: center;
  }
  .brand__name {
    font-family: "Oswald", sans-serif;
    font-weight: 500;
    font-size: 20px;
    line-height: 1.2;
    letter-spacing: 1px;
    text-transform: uppercase;
    color: var(--ink);
  }

  .person {
    position: absolute;
    left: 237px;
    top: 116px;
    width: 202px;
    text-align: center;
  }
  .rule {
    height: 1px;
    background: linear-gradient(90deg, rgba(255,255,255,0.15), rgba(255,255,255,0.9) 15%, rgba(255,255,255,0.9) 85%, rgba(255,255,255,0.15));
  }
  .person__name {
    font-weight: 400;
    font-size: 30px;
    line-height: 37px;
    letter-spacing: 0.5px;
    text-transform: uppercase;
  }
  .person__role {
    margin-top: 3px;
    font-weight: 500;
    font-size: 12px;
    line-height: 16px;
    letter-spacing: 0.3px;
    text-transform: uppercase;
  }
</style>
</head>
<body>
<main class="sheet">
  <section class="card card--top">
    <div class="brand"><span class="brand__name">Quillmere<br>Farm</span></div>
    <div class="person">
      <div class="rule"></div>
      <h1 class="person__name">Alder Vossen</h1>
      <div class="rule"></div>
      <p class="person__role">President/Owner</p>
    </div>
  </section>

  <section class="card card--bottom">
    <div class="brand"><span class="brand__name">Quillmere<br>Farm</span></div>
    <div class="person">
      <div class="rule"></div>
      <h2 class="person__name">Alder Vossen</h2>
      <div class="rule"></div>
      <p class="person__role">President/Owner</p>
    </div>
  </section>
</main>
</body>
</html>
```